KELPO's Coffee Liqueur Shot Arabica

Need a lable for a 500ml bottle of homemade Coffee liqueur.
Name:
KELPO's
Coffee
Shot

Shape: Round, 80mm
Color of the lable should be black and letters in black.
Letters KELPO's min 12mm hight.
Color of the liqueur is dark brown.
Add: 500ml
Add: 38% vol.
Should have a bean on the lable.
Maybe some bullet words on the bottom...
Prefered design see Pic1a with bottle.

Target Market(s)

People that enjoy coffee in shots, in coctails, with ice or on top of icecream or any other dessert

Font styles to use
Serif

Colors

Designer to choose colors to be used in the design.

Requirements
Must have
• See Pic 1a
Nice to have
• See Pic1a (bottle)
Should not have
• Different colors

```html
<!DOCTYPE html>
<html lang="en">
<head>
<meta charset="utf-8">
<title>KELPO's Coffee Shot – Round Label</title>
<link href="https://fonts.googleapis.com/css2?family=Oswald:wght@500;600;700&family=Kaushan+Script&display=swap" rel="stylesheet">
<style>
  :root {
    --ink: #111111;
    --paper: #ffffff;
    --backdrop: #f4f4f2;
  }
  html, body {
    margin: 0;
    padding: 0;
    width: 849px;
    height: 1200px;
    overflow: hidden;
    background: var(--backdrop);
  }
  .canvas {
    width: 849px;
    height: 1200px;
    display: flex;
    align-items: center;
    justify-content: center;
  }
  .label {
    width: 660px;
    height: 660px;
    display: block;
  }
  .label-face { fill: var(--paper); }
  .ring-outer { fill: none; stroke: var(--ink); stroke-width: 2.5; }
  .ring-inner { fill: none; stroke: var(--ink); stroke-width: 1.2; }
  .rule { fill: none; stroke: var(--ink); stroke-width: 1.6; }
  .center-disc { fill: var(--ink); }
  .center-ring { fill: none; stroke: var(--paper); stroke-width: 1.5; }
  .brand-name {
    font-family: "Oswald", "Arial Narrow", sans-serif;
    font-weight: 700;
    font-size: 78px;
    letter-spacing: 3px;
    fill: var(--ink);
  }
  .product-script {
    font-family: "Kaushan Script", cursive;
    font-size: 86px;
    fill: var(--paper);
  }
  .product-type {
    font-family: "Oswald", "Arial Narrow", sans-serif;
    font-weight: 700;
    font-size: 64px;
    letter-spacing: 1px;
    fill: var(--paper);
  }
  .spec {
    font-family: "Oswald", "Arial Narrow", sans-serif;
    font-weight: 600;
    font-size: 19px;
    fill: var(--ink);
  }
  .keyword {
    font-family: "Oswald", "Arial Narrow", sans-serif;
    font-weight: 600;
    font-size: 24px;
    letter-spacing: 3px;
    fill: var(--ink);
  }
  .bean { fill: var(--ink); }
</style>
</head>
<body>
<main class="canvas">
  <svg class="label" viewBox="0 0 640 640" xmlns="http://www.w3.org/2000/svg" aria-label="KELPO's Coffee Shot round label">
    <defs>
      <path id="arc-top" d="M 100,320 A 220 220 0 0 1 540,320"/>
      <path id="arc-bottom" d="M 44,320 A 276 276 0 0 0 596,320"/>
    </defs>

    <circle class="label-face" cx="320" cy="320" r="317"/>
    <circle class="ring-outer" cx="320" cy="320" r="316"/>
    <circle class="ring-inner" cx="320" cy="320" r="309"/>

    <text class="brand-name" text-anchor="middle">
      <textPath href="#arc-top" startOffset="50%">KELPO'S</textPath>
    </text>

    <g class="center-badge">
      <circle class="center-disc" cx="320" cy="320" r="164"/>
      <circle class="center-ring" cx="320" cy="320" r="157"/>
      <text class="product-script" x="320" y="320" text-anchor="middle">Coffee</text>
      <text class="product-type" x="320" y="420" text-anchor="middle">SHOT</text>
    </g>

    <g class="spec-left">
      <line class="rule" x1="44" y1="248" x2="92" y2="248"/>
      <text class="spec" x="68" y="275" text-anchor="middle">38%</text>
      <text class="spec" x="68" y="298" text-anchor="middle">VOL</text>
      <line class="rule" x1="44" y1="322" x2="92" y2="322"/>
    </g>
    <g class="spec-right">
      <line class="rule" x1="548" y1="248" x2="596" y2="248"/>
      <text class="spec" x="572" y="275" text-anchor="middle">500</text>
      <text class="spec" x="572" y="298" text-anchor="middle">ML</text>
      <line class="rule" x1="548" y1="322" x2="596" y2="322"/>
    </g>

    <path class="rule" d="M 92,322 A 228 228 0 0 0 278,546"/>
    <path class="rule" d="M 548,322 A 228 228 0 0 1 362,546"/>

    <ellipse class="bean" role="img" aria-label="Coffee bean" cx="320" cy="552" rx="24" ry="33" transform="rotate(35 320 552)"/>

    <text class="keyword" text-anchor="middle">
      <textPath href="#arc-bottom" startOffset="24%">ARABICA</textPath>
    </text>
    <text class="keyword" text-anchor="middle">
      <textPath href="#arc-bottom" startOffset="76%">INTENSIV</textPath>
    </text>
  </svg>
</main>
</body>
</html>
```